Flyer Design Project with menu

We are from Juniper Table Restaurant. We usually serve breakfast, soul food, fried and BBQ Ribs , legs, wings etc. We located at 2873 n. Willow avenue, canton, 39046, MS. Since this is a new restaurant we want to let people know about us. Please create a good professional flyer including menu on that. Thank you. Please let us know if you need any other information.
Updates

Target Market(s)

We want to attract customers from 3 different locations near 15 miles radius.

Industry/Entity Type

American Restaurant

Font styles to use
Serif

Requirements
Must have
• Good graphics with food pictures.
• Soul food graphic pictures, RIBS, FISH and breakfast regular.
Nice to have
• 20% discount coupon offer.

```html
<!DOCTYPE html>
<html lang="en">
<head>
<meta charset="utf-8">
<title>Juniper Table Restaurant — Menu Flyer</title>
<link href="https://fonts.googleapis.com/css2?family=Cinzel:wght@400;700&family=Roboto+Condensed:wght@400&family=Pinyon+Script&display=swap" rel="stylesheet">
<style>
  :root{
    --red:#b3282c;
    --red-text:#b0282c;
    --tan:#c9874a;
    --beige:#e6d59c;
    --olive:#9aa02a;
    --rose:#c27a8b;
    --cream-border:#ecd6a0;
    --white:#ffffff;
    --ink:#2a2a2a;
    --dots:#555555;
  }
  *{box-sizing:border-box;margin:0;padding:0}
  html,body{width:1200px;height:848px;overflow:hidden;background:#fff}
  .flyer{position:relative;width:1200px;height:848px;overflow:hidden;font-family:"Roboto Condensed",Arial Narrow,sans-serif;color:var(--ink)}
  .panel{position:absolute}
  .photo{position:absolute}

  /* photo areas */
  .photo--ham{left:0;top:0;width:400px;height:204px;background:radial-gradient(ellipse at 45% 50%,#b8584e 0%,#c99a62 45%,#d9a872 100%)}
  .photo--rice{left:400px;top:0;width:400px;height:204px;background:radial-gradient(ellipse at 50% 55%,#9a5a2c 0%,#6f7d2e 45%,#e9e2d4 100%)}
  .photo--eggs{left:0;top:610px;width:400px;height:238px;background:linear-gradient(160deg,#8fb15c 0%,#e9e3dc 40%,#d9a08a 70%,#f2eeea 100%)}
  .photo--curry{left:400px;top:610px;width:400px;height:238px;background:linear-gradient(120deg,#efe9df 0%,#7a4320 35%,#b07a46 70%,#d7b28a 100%)}
  .photo--dessert{left:800px;top:610px;width:400px;height:238px;background:radial-gradient(ellipse at 45% 55%,#f4eee6 0%,#e66a5a 45%,#c9a59a 100%)}

  /* panels */
  .panel--breakfast{left:0;top:204px;width:400px;height:406px;background:var(--red);color:var(--white)}
  .panel--lunch{left:400px;top:204px;width:400px;height:406px;background:var(--white)}
  .panel--grill{left:800px;top:0;width:400px;height:610px;background:var(--beige)}

  /* badges */
  .badge{position:absolute;border-radius:50%;border:3px solid var(--white);display:flex;align-items:center;justify-content:center;text-align:center;font-family:"Cinzel",Georgia,serif;color:var(--white);line-height:1.2}
  .badge--breakfast{left:26px;top:188px;width:236px;height:92px;background:var(--tan);font-size:16.5px}
  .badge--cooked{left:34px;top:587px;width:200px;height:68px;background:var(--olive);font-size:14.5px;line-height:1.15}
  .badge--plate{left:544px;top:442px;width:240px;height:100px;background:var(--red);border-color:var(--cream-border);font-size:13.5px;line-height:1.3;padding:0 12px}
  .badge--dessert{left:992px;top:590px;width:188px;height:76px;background:var(--rose);font-size:16.5px;line-height:1.2}

  /* breakfast */
  .plate-price{position:absolute;left:32px;top:100px;font-family:"Cinzel",Georgia,serif;font-size:14px;line-height:19px}
  .plate-price strong{font-size:20px;font-weight:400}
  .menu-list{position:absolute;list-style:none}
  .row{display:flex;align-items:baseline;white-space:nowrap}
  .row .dots{flex:1;border-bottom:1.5px dotted currentColor;margin:0 4px 3px;opacity:.85}
  .breakfast-list{left:32px;top:160px;width:334px;font-size:14px}
  .breakfast-list .row{height:18.5px}

  /* lunch */
  .lunch-intro{position:absolute;left:28px;top:10px;font-family:"Cinzel",Georgia,serif;color:var(--red-text);font-size:15px;line-height:19px}
  .lunch-intro strong{font-size:21px;font-weight:400}
  .lunch-title{position:absolute;left:28px;top:56px;font-family:"Cinzel",Georgia,serif;color:var(--red-text);font-size:15px}
  .numbered{position:absolute;left:26px;list-style:none;font-size:14px;line-height:18.5px}
  .numbered--entrees{top:81px}
  .sides-label{position:absolute;left:26px;top:211px;font-size:14px;color:var(--red-text)}
  .numbered--sides{top:229px}

  /* grill */
  .grill-section{position:absolute;left:30px;width:332px}
  .grill-section h2{font-family:"Cinzel",Georgia,serif;font-weight:400;color:var(--red-text);font-size:15px;line-height:20px;margin-bottom:3px}
  .grill-section .row{height:17px;font-size:14px}
  .strips-grid{display:grid;grid-template-columns:152px 148px;column-gap:32px}
  .thanks{position:absolute;left:0;width:400px;top:552px;text-align:center;font-family:"Pinyon Script",cursive;color:var(--red-text);font-size:22px}
</style>
</head>
<body>
<div class="flyer">
  <div class="photo photo--ham" role="img" aria-label="Cured ham with sliced prosciutto on a wooden board"></div>
  <div class="photo photo--rice" role="img" aria-label="Stir-fried rice with chicken, peppers and green onion"></div>

  <section class="panel panel--breakfast">
    <p class="plate-price">Plate sold at <strong>4.99</strong><br>or items sold separately</p>
    <ul class="menu-list breakfast-list">
      <li class="row"><span>Grits</span><span class="dots"></span><span>1.99</span></li>
      <li class="row"><span>Eggs</span><span class="dots"></span><span>1.99</span></li>
      <li class="row"><span>Sausage Patties - 2 for</span><span class="dots"></span><span>1.99</span></li>
      <li class="row"><span>Smoked link Sausage 2 for</span><span class="dots"></span><span>1.99</span></li>
      <li class="row"><span>Hashbrowns</span><span class="dots"></span><span>1.99</span></li>
      <li class="row"><span>Biscuits</span><span class="dots"></span><span>1.99</span></li>
      <li class="row"><span>Baked HAM</span><span class="dots"></span><span>1.99</span></li>
      <li class="row"><span>Bacon</span><span class="dots"></span><span>1.99</span></li>
      <li class="row"><span>PAN CAKE</span><span class="dots"></span><span>1.99</span></li>
      <li class="row"><span>Sandwiches</span><span class="dots"></span><span>2.99</span></li>
    </ul>
  </section>

  <section class="panel panel--lunch">
    <p class="lunch-intro">Order from the menu or create a plate<br>from the line for only <strong>7.99</strong></p>
    <h2 class="lunch-title">Lunch and Dinner Menu: (Soul Food)</h2>
    <ol class="numbered numbered--entrees">
      <li>1. Red beans with rice and sausage</li>
      <li>2. Beef tips with rice.</li>
      <li>3. Turkey Necks</li>
      <li>4. Fried \ Baked chicken.</li>
      <li>5. Spaghetti</li>
      <li>6. Stuffed bell pepper ( Shrimp, Crab and sausage )</li>
      <li>7. Chicken on a stick</li>
    </ol>
    <p class="sides-label">SIDES:</p>
    <ol class="numbered numbered--sides">
      <li>1. Rice</li>
      <li>2. Mac N Cheese.</li>
      <li>3. Collard Greens.</li>
      <li>4. String Beans.</li>
      <li>5. BBQ red beans.</li>
      <li>6. Mash Potatoes.</li>
      <li>7. Corn Bread</li>
      <li>8. Green Beans.</li>
      <li>9. Corn.</li>
    </ol>
  </section>

  <section class="panel panel--grill">
    <div class="grill-section" style="top:36px">
      <h2>Salads</h2>
      <div class="row"><span>Chef Salad</span><span class="dots"></span><span>7.00</span></div>
      <div class="row"><span>Grilled Chicken Salad</span><span class="dots"></span><span>7.50</span></div>
      <div class="row"><span>Popcorn Chicken Salad</span><span class="dots"></span><span>7.50</span></div>
    </div>
    <div class="grill-section" style="top:133px">
      <h2>Burgers</h2>
      <div class="row"><span>Classic Burger</span><span class="dots"></span><span>5.00</span></div>
      <div class="row"><span>Classic Cheeseburger</span><span class="dots"></span><span>6.00</span></div>
      <div class="row"><span>Bacon and Cheeseburger</span><span class="dots"></span><span>7.00</span></div>
    </div>
    <div class="grill-section" style="top:218px">
      <h2>Fried Chicken</h2>
      <div class="row"><span>Served with 2sides Individual</span><span class="dots"></span><span>2.00</span></div>
      <div class="row"><span>2 pc White</span><span class="dots"></span><span>6.99</span></div>
      <div class="row"><span>2pc Dark</span><span class="dots"></span><span>4.99</span></div>
    </div>
    <div class="grill-section" style="top:304px">
      <h2>Strips</h2>
      <div class="strips-grid">
        <div class="row"><span>3pc</span><span class="dots"></span><span>3.95</span></div>
        <div class="row"><span>meal</span><span class="dots"></span><span>5.99</span></div>
        <div class="row"><span>6pc</span><span class="dots"></span><span>7.00</span></div>
        <div class="row"><span>meal</span><span class="dots"></span><span>8.99</span></div>
        <div class="row"><span>9pc</span><span class="dots"></span><span>10.99</span></div>
        <div class="row"><span>meal</span><span class="dots"></span><span>12.99</span></div>
      </div>
    </div>
    <div class="grill-section" style="top:390px">
      <h2>Ribs</h2>
      <div class="row"><span>Full Rack</span><span class="dots"></span><span>16.99</span></div>
      <div class="row"><span>Half Rack</span><span class="dots"></span><span>8.99</span></div>
    </div>
    <div class="grill-section" style="top:458px">
      <h2>Seafood</h2>
      <div class="row"><span>2pc Fried Fish</span><span class="dots"></span><span>8.99</span></div>
      <div class="row"><span>6pc shrimp</span><span class="dots"></span><span>6.99</span></div>
      <div class="row"><span>12pc shrimp</span><span class="dots"></span><span>11.99</span></div>
    </div>
    <p class="thanks">We appreciate your business. Thank You!</p>
  </section>

  <div class="photo photo--eggs" role="img" aria-label="Poached egg and bacon on toast with side salad"></div>
  <div class="photo photo--curry" role="img" aria-label="Chicken curry with rice and grilled vegetables beside a small salad"></div>
  <div class="photo photo--dessert" role="img" aria-label="Panna cotta dessert with strawberry sauce and berries"></div>

  <div class="badge badge--breakfast">Start your day<br>with us!!! Breakfast<br>starting at 6am</div>
  <div class="badge badge--cooked">Everything is<br>cook to order on<br>our menu</div>
  <div class="badge badge--plate">Plate consist of an entrée or a meat, 2 sides, a bread and drink of the day</div>
  <div class="badge badge--dessert">Try the Dessert<br>of the Day!</div>
</div>
</body>
</html>
```